Buchcover für ein Buch über Heilung/Alternative Heilung/Tranceheilung/Geistheilung
Zielgruppe
Ich bin Buchautorin, Medium und Coach und suche für mein nächstes Buch, über Heilung, dass ich gemeinsam mit meinem Mann schreibe, ein Buchcover. Ich habe die Cover der bereits erschienen Bücher angefügt und ein Bild,von Pixelgrund beigefügt, dass mir gefällt von den Farben her. Es darf aber auch gerne etwas ähnliches sein. Farben sollen frisch sein. Kaufe das Foto dann selbstverständlich in der richtigen Lizenz.
Aufgabenstellung
Das Design soll frisch sein und Gesundheit ausstrahlen. Titel wird sein: Sternenstaub, Morgentau und Stille Gärten
Slogan: Den habe ich noch nicht. Sollte inhaltlich folgendes aussagen. Heilung kann einfach sein, Heilung verstehen, Programmieren Sie sich auf Gesundheit und Heilung auf allen Ebenen
(so in etwa)
Verlag: Birkenwald Verlag ( Logo liegt bei)
Autoren: Liska und Tomas Brendel
Freue mich auf viele Vorschläge.

```html
<!DOCTYPE html>
<html lang="de">
<head>
<meta charset="utf-8">
<title>Sternenstaub, Morgentau und Stille Gärten – Buchcover</title>
<link rel="stylesheet" href="https://fonts.googleapis.com/css2?family=Great+Vibes&family=Tinos&family=Noto+Serif&family=Cormorant+SC:wght@600&display=swap">
<style>
  :root {
    --page-bg: #ffffff;
    --sky-top: #078ddf;
    --sky-mid: #1a9be6;
    --sky-bottom: #7fccf4;
    --glow: #ffffff;
    --title-yellow: #f8f200;
    --title-shadow: rgba(20, 40, 70, 0.75);
    --text-white: #ffffff;
  }
  * { margin: 0; padding: 0; box-sizing: border-box; }
  html, body {
    width: 975px;
    height: 1200px;
    overflow: hidden;
    background: var(--page-bg);
  }
  .canvas {
    position: relative;
    width: 975px;
    height: 1200px;
  }
  .cover {
    position: absolute;
    left: 137px;
    top: 75px;
    width: 700px;
    height: 1050px;
    overflow: hidden;
    background: linear-gradient(180deg, var(--sky-top) 0%, var(--sky-mid) 45%, var(--sky-bottom) 100%);
    box-shadow: 0 18px 40px rgba(0, 0, 0, 0.18);
  }
  .cover-illustration {
    position: absolute;
    left: 0;
    top: 420px;
    width: 700px;
    height: 630px;
  }
  .cover-illustration svg { display: block; width: 100%; height: 100%; }
  .title {
    position: absolute;
    left: 0;
    top: 110px;
    width: 100%;
    font-family: "Great Vibes", cursive;
    font-weight: 400;
    color: var(--title-yellow);
    text-shadow: 2px 3px 2px var(--title-shadow);
    line-height: 1;
  }
  .title-line { display: block; font-size: 104px; }
  .title-line--first { padding-left: 40px; }
  .title-line--second { padding-left: 170px; margin-top: -6px; }
  .subtitle {
    position: absolute;
    left: 0;
    top: 380px;
    width: 100%;
    padding-left: 170px;
    font-family: "Tinos", serif;
    font-size: 38px;
    letter-spacing: -1px;
    color: var(--text-white);
    text-shadow: 1px 2px 2px var(--title-shadow);
  }
  .tagline {
    position: absolute;
    right: 40px;
    top: 850px;
    text-align: right;
    font-family: "Noto Serif", serif;
    font-size: 30px;
    line-height: 1.2;
    color: var(--text-white);
    text-shadow: 1px 2px 2px var(--title-shadow);
  }
  .authors {
    position: absolute;
    right: 40px;
    top: 950px;
    font-family: "Cormorant SC", serif;
    font-weight: 600;
    font-size: 30px;
    color: var(--title-yellow);
    text-shadow: 1px 2px 2px var(--title-shadow);
  }
</style>
</head>
<body>
<div class="canvas">
  <section class="cover">
    <div class="cover-illustration" role="img" aria-label="Zwei geöffnete Hände halten ein strahlendes Licht vor weißen Wolken am blauen Himmel">
      <svg viewBox="0 0 700 630" preserveAspectRatio="none" aria-hidden="true">
        <defs>
          <radialGradient id="lightGlow" cx="0.45" cy="0.5" r="0.55">
            <stop offset="0" stop-color="#ffffff" stop-opacity="0.95"/>
            <stop offset="0.45" stop-color="#e6f5fd" stop-opacity="0.7"/>
            <stop offset="1" stop-color="#8fd2f5" stop-opacity="0"/>
          </radialGradient>
          <linearGradient id="warmTone" x1="0" y1="0" x2="0" y2="1">
            <stop offset="0" stop-color="#f3c6a6" stop-opacity="0"/>
            <stop offset="1" stop-color="#f0c3a2" stop-opacity="0.35"/>
          </linearGradient>
        </defs>
        <rect width="700" height="630" fill="url(#lightGlow)"/>
        <rect width="700" height="630" fill="url(#warmTone)"/>
      </svg>
    </div>

    <h1 class="title">
      <span class="title-line title-line--first">Sternenstaub,</span>
      <span class="title-line title-line--second">Morgentau</span>
    </h1>
    <p class="subtitle">und Stille Gärten</p>

    <p class="tagline">Lorem ipsum dolor<br>sit amet.</p>
    <p class="authors">Liska und Tomas Brendel</p>
  </section>
</div>
</body>
</html>
```